Latin CBD company needs a design for a counter display box

-We would like a design for a display box for our restorative CBD oil tinctures. We would like to stand out our brand promoting wellness being and health. However, because its targeting the latin market, we would like to see color on it.
- The display box is for CBD tinctures (image attached)
-I am attaching two files, if you are Spanish speaker it would be nice to see the design in Spanish. Thank you!
THANK YOU IN ADVANCE FOR WORKING IN OUR PROJECT!

Font styles to use
Serif
Sans Serif

```html
<!DOCTYPE html>
<html lang="es">
<head>
<meta charset="utf-8">
<title>Solvida CBD – Caja exhibidora</title>
<link rel="stylesheet" href="https://fonts.googleapis.com/css2?family=Montserrat:wght@500&family=Varela+Round&family=Nunito:wght@800&display=swap">
<style>
  :root {
    --leaf-green: #7fc770;
    --grape: #662974;
    --sun-yellow: #f7e11b;
    --white: #ffffff;
    --guide-blue: #1aa3de;
  }
  html, body {
    margin: 0;
    padding: 0;
    width: 1200px;
    height: 1200px;
    overflow: hidden;
    background: var(--white);
  }
  .dieline { display: block; width: 1200px; height: 1200px; }
  .panel-top { fill: var(--leaf-green); }
  .panel-base { fill: var(--grape); }
  .brand-ring { fill: none; stroke: var(--grape); stroke-width: 2; }
  .seal { fill: var(--white); stroke: var(--white); stroke-width: 0; }
  .seal-ring { fill: none; stroke: var(--white); stroke-width: 1.6; }
  .brand-name {
    font-family: "Montserrat", sans-serif;
    font-weight: 500;
    font-size: 33px;
    fill: var(--grape);
    text-anchor: middle;
  }
  .product-title {
    font-family: "Nunito", sans-serif;
    font-weight: 800;
    font-size: 21px;
    fill: var(--sun-yellow);
    text-anchor: middle;
  }
  .product-sub {
    font-family: "Varela Round", sans-serif;
    font-size: 21px;
    fill: var(--white);
    text-anchor: middle;
  }
  .product-note {
    font-family: "Varela Round", sans-serif;
    font-size: 18px;
    fill: var(--grape);
    text-anchor: middle;
  }
  .benefit {
    font-family: "Nunito", sans-serif;
    font-weight: 800;
    font-size: 11px;
    fill: var(--white);
  }
  .fold-line { stroke: var(--guide-blue); stroke-width: 1.2; stroke-dasharray: 5 4; fill: none; }
  .edge-line { stroke: var(--leaf-green); stroke-width: 1; stroke-dasharray: 4 4; fill: none; opacity: .7; }
</style>
</head>
<body>
<svg class="dieline" viewBox="0 0 1200 1200" xmlns="http://www.w3.org/2000/svg">

  <!-- Front header panel -->
  <g class="header-panel">
    <path class="panel-top" d="M124 189 H241 A160 160 0 0 1 469 189 H587 V346 H124 Z"/>
    <path class="panel-base" d="M124 346 H587 L576 538 H135 Z"/>
    <circle class="brand-ring" cx="355" cy="184" r="32.5"/>
    <circle class="seal-ring" cx="167" cy="232" r="31"/>
    <circle class="seal" cx="167" cy="232" r="22"/>
    <text class="brand-name" x="355" y="245">SOLVIDA CBD</text>
    <text class="product-title" x="355" y="283">Aceite Restaurador de CBD</text>
    <text class="product-sub" x="355" y="310">Hemp Oil Extract</text>
    <text class="product-note" x="355" y="334">No Psicoactivo</text>
  </g>

  <!-- Back header panel -->
  <g class="header-panel">
    <path class="panel-top" d="M621 189 H739 A160 160 0 0 1 967 189 H1084 V346 H621 Z"/>
    <path class="panel-base" d="M621 346 H1084 L1073 538 H632 Z"/>
    <circle class="brand-ring" cx="852.5" cy="184" r="32.5"/>
    <circle class="seal-ring" cx="669" cy="243" r="31"/>
    <circle class="seal" cx="669" cy="243" r="22"/>
    <text class="brand-name" x="852.5" y="245">SOLVIDA CBD</text>
    <text class="product-title" x="852.5" y="283">Aceite Restaurador de CBD</text>
    <text class="product-sub" x="852.5" y="310">Hemp Oil Extract</text>
    <text class="product-note" x="852.5" y="334">No Psicoactivo</text>
  </g>

  <!-- Side panel -->
  <g class="side-panel">
    <rect class="panel-top" x="436" y="590" width="336" height="400"/>
    <rect class="panel-base" x="436" y="990" width="336" height="124"/>
    <line class="fold-line" x1="772" y1="590" x2="436" y2="989"/>
    <line class="edge-line" x1="772" y1="590" x2="772" y2="989"/>
    <circle class="brand-ring" cx="637.5" cy="903" r="32.5"/>
    <text class="brand-name" x="637.5" y="966">SOLVIDA CBD</text>
    <text class="benefit" x="453" y="1026">• 100% Colorado Grown Organic Hemp</text>
    <text class="benefit" x="453" y="1046">• Promote a healthy Endocannabinoid System</text>
    <text class="benefit" x="453" y="1066">• Full Spectrum</text>
    <text class="benefit" x="453" y="1086">• Non Psychoactive</text>
  </g>
</svg>
</body>
</html>
```